Business card for new consulting business - Brackenvale Enterprises Pty Ltd.

Consulting in the areas of Occupational Health, Safety and Community Relations in the resources (mining) industries. The consultant (me) will work both within Australia and overseas jurisdictions such as South East Asia, Africa , South America etc, often working with third world indigenous communities. The design should suggest a high level of social and environmental responsibility.

```html
<!DOCTYPE html>
<html lang="en">
<head>
<meta charset="utf-8">
<title>Brackenvale Enterprises – Business Card</title>
<link href="https://fonts.googleapis.com/css2?family=Lato:wght@400;700&family=Ubuntu:wght@500;700&display=swap" rel="stylesheet">
<style>
  :root {
    --backdrop: #2e3033;
    --card-white: #ffffff;
    --card-grey: #ececec;
    --brand-blue: #0b6fc0;
    --brand-deep: #1c3f8f;
    --brand-sky: #03a3e3;
    --text-grey: #4a4d52;
    --rule-grey: #7d8790;
    --mark-silver: #d9dde2;
  }
  * { margin: 0; padding: 0; box-sizing: border-box; }
  html, body { width: 1200px; height: 900px; overflow: hidden; }
  body {
    background: var(--backdrop);
    font-family: "Lato", sans-serif;
    position: relative;
  }
  .card {
    position: absolute;
    left: 250px;
    width: 700px;
    height: 400px;
    box-shadow: 0 14px 30px rgba(0,0,0,0.45);
  }
  .card-front {
    top: 30px;
    background: radial-gradient(ellipse at 55% 60%, var(--card-white) 0%, var(--card-white) 45%, var(--card-grey) 100%);
  }
  .card-back {
    top: 470px;
    background: linear-gradient(135deg, var(--brand-deep) 0%, var(--brand-blue) 55%, var(--brand-sky) 100%);
    display: flex;
    align-items: center;
    justify-content: center;
  }
  .brand {
    position: absolute;
    left: 60px;
    top: 140px;
    display: flex;
    align-items: center;
    gap: 14px;
  }
  .brand-square {
    width: 44px;
    height: 44px;
    background: var(--brand-blue);
    flex: none;
  }
  .brand-name {
    font-family: "Lato", sans-serif;
    font-weight: 700;
    font-size: 24px;
    line-height: 1.15;
    color: var(--brand-blue);
    width: 200px;
  }
  .divider {
    position: absolute;
    left: 340px;
    top: 95px;
    width: 2px;
    height: 215px;
    background: var(--rule-grey);
  }
  .details {
    position: absolute;
    left: 372px;
    top: 95px;
    color: var(--text-grey);
  }
  .person-name {
    font-family: "Ubuntu", sans-serif;
    font-weight: 700;
    font-size: 32px;
    color: var(--brand-blue);
    letter-spacing: 0.5px;
    line-height: 1.1;
  }
  .person-role {
    font-size: 17px;
    margin-bottom: 16px;
  }
  .address { font-size: 17px; line-height: 1.3; margin-bottom: 14px; }
  .contact-list { list-style: none; font-size: 17px; line-height: 1.4; }
  .contact-list li { display: flex; align-items: center; gap: 10px; }
  .contact-list svg { width: 13px; height: 13px; flex: none; }
  .back-brand { display: flex; align-items: center; gap: 18px; }
  .back-brand .brand-square { background: var(--mark-silver); width: 56px; height: 56px; }
  .back-brand .brand-name { color: var(--mark-silver); font-size: 32px; width: auto; }
</style>
</head>
<body>
  <section class="card card-front">
    <div class="brand">
      <span class="brand-square"></span>
      <span class="brand-name">Brackenvale Enterprises Pty Ltd</span>
    </div>
    <div class="divider"></div>
    <div class="details">
      <h1 class="person-name">Darren Kowal</h1>
      <p class="person-role">Founder</p>
      <p class="address">48 Ridgeline Ave.<br>Kalgoorlie, WA 6430</p>
      <ul class="contact-list">
        <li>
          <svg viewBox="0 0 16 16" aria-hidden="true"><path fill="#0b6fc0" d="M4 1l2.5 3-1.5 1.5c.8 2 2.5 3.7 4.5 4.5L11 8.5l3 2.5-1.5 2.8C7.5 13.5 2.5 8.5 1.2 2.5z"/></svg>
          08-9021-4476
        </li>
        <li>
          <svg viewBox="0 0 16 16" aria-hidden="true"><rect x="1" y="3" width="14" height="10" fill="none" stroke="#0b6fc0" stroke-width="1.6"/><path d="M1 3l7 6 7-6" fill="none" stroke="#0b6fc0" stroke-width="1.6"/></svg>
          info@brackenvaleenterprises.com
        </li>
        <li>
          <svg viewBox="0 0 16 16" aria-hidden="true"><circle cx="8" cy="8" r="7" fill="#0b6fc0"/><path d="M1 8h14M8 1c-3 3-3 11 0 14M8 1c3 3 3 11 0 14" fill="none" stroke="#fff" stroke-width="1"/></svg>
          www.brackenvaleenterprises.com
        </li>
      </ul>
    </div>
  </section>

  <section class="card card-back">
    <div class="back-brand">
      <span class="brand-square"></span>
      <span class="brand-name">Brackenvale Enterprises Pty Ltd</span>
    </div>
  </section>
</body>
</html>
```